Willowmere Equine Sanctuary Flyer Urgent

Willowmere Equine Sanctuary

Rescue • Rehabilitation • Sanctuary

Willowmere Equine Sanctuary provides a safe and ethical refuge for horses, ponies and donkeys who have nowhere else to go. Some arrive needing rehabilitation and careful retraining, while others find permanent sanctuary here due to age, injury or behavioural needs.

Our mission is simple: to improve the physical and psychological wellbeing of every animal in our care.

At Willowmere we focus on:
• Rescue and rehabilitation of horses in need
• Lifetime sanctuary for those who cannot be rehomed
• Education and advocacy for responsible horse care
• Equine rehabilitation services to help horses recover and thrive

Sponsor a Horse

One of the most meaningful ways to support our work is by sponsoring one of our residents. Each horse, pony or donkey only has one sponsor!

Your sponsorship helps provide:
• Hay and feed
• Veterinary care
• Hoof trimming and routine health care
• Rugs, shelter and daily care

Many of our horses will live out their lives here, and sponsorship ensures they are safe, well fed and cared for every single day.

Sponsorship starts from $15 - $25 per week / $60 -$100 per month.

How You Can Help

• Sponsor a horse
• Make a donation
• Share our work with others

Your support helps us continue to say yes to horses who need a second chance.

📍 Willowmere Park, Victoria
📧 clara@willowmerepark-example.org

📞 0400 519 627

Font styles to use
Serif
Sans Serif

Colors
F0912C
F2A743
F7CA91
FBE8D2
FDF5EE
EE7325
F08F49
F5BC92
FAE3D3
FDF4ED

Requirements
Should not have
• Photos not provided by Willowmere

```html
<!DOCTYPE html>
<html lang="en">
<head>
<meta charset="utf-8">
<title>Willowmere Equine Sanctuary Flyer</title>
<link href="https://fonts.googleapis.com/css2?family=Cinzel:wght@400;700;900&family=Open+Sans:wght@400;600;700;800&display=swap" rel="stylesheet">
<style>
  :root{
    --orange:#EE7325;
    --orange-light:#F0912C;
    --amber:#F2A743;
    --cream:#FAE3D3;
    --peach:#F5BC92;
    --ink:#1c1c1c;
    --white:#ffffff;
    --page:#ffffff;
  }
  *{margin:0;padding:0;box-sizing:border-box}
  html,body{width:1200px;height:1200px;overflow:hidden;background:var(--page)}
  body{position:relative;font-family:"Open Sans",Arial,sans-serif;color:var(--ink)}
  .flyer{position:absolute;left:251px;top:107px;width:697px;height:985px;background:var(--white);overflow:hidden;box-shadow:0 6px 24px rgba(0,0,0,.25)}
  .shapes{position:absolute;inset:0;width:697px;height:985px}
  .abs{position:absolute}
  .title{left:0;width:697px;top:50px;text-align:center;font-family:"Cinzel",Georgia,serif;font-weight:700;font-size:37px;line-height:44px;color:var(--white);text-shadow:0 2px 4px rgba(0,0,0,.35)}
  .tagline{left:0;width:697px;top:139px;text-align:center;font-weight:700;font-size:18.5px;color:var(--white);letter-spacing:.2px}
  .intro{left:95px;width:510px;top:168px;text-align:center;font-size:12.4px;line-height:15.6px;color:var(--white)}
  .price-badge{left:42px;top:286px;width:200px;text-align:center;color:var(--ink)}
  .price-badge .lead{font-weight:700;font-size:19px;line-height:24px}
  .price-badge .amount{font-weight:800;font-size:25px;line-height:28px;margin-top:4px}
  .price-badge .unit{font-size:18px;line-height:18px}
  .price-badge .amount.second{margin-top:6px}
  .sponsor-note{left:41px;top:490px;width:196px;font-weight:700;font-size:12.6px;line-height:16.5px;color:var(--white)}
  .provide-head{left:40px;top:606px;font-family:"Cinzel",Georgia,serif;font-weight:900;font-size:19px;line-height:26px;color:var(--ink)}
  .provide-list{left:40px;top:664px;list-style:none;color:var(--white);font-weight:700;font-size:15.5px;line-height:19px}
  .provide-list li{display:flex;gap:7px;margin-bottom:2px}
  .provide-list svg{flex:none;margin-top:4px}
  .mission-head{left:292px;width:350px;top:292px;text-align:center;font-family:"Cinzel",Georgia,serif;font-weight:900;font-size:26px;color:var(--orange-light)}
  .mission-body{left:272px;width:395px;top:331px;text-align:center;font-family:"Cinzel",Georgia,serif;font-size:18.5px;line-height:23px;color:var(--ink);text-transform:uppercase}
  .divider{left:358px;top:404px;width:200px;border-top:1.5px dotted #666}
  .focus-head{left:306px;top:416px;font-weight:700;font-size:16.5px;color:var(--ink)}
  .focus-list{left:303px;top:440px;list-style:none;font-size:14px;line-height:22.4px;color:var(--ink)}
  .focus-list li{display:flex;gap:6px}
  .focus-list svg{flex:none;margin-top:7px}
  .help-tag{left:364px;top:580px;width:216px;height:29px;background:var(--orange);color:var(--white);font-weight:700;font-size:17.5px;line-height:29px;text-align:center}
  .help-item{top:626px;display:flex;gap:4px;font-weight:700;font-size:13.2px;line-height:17px;color:var(--ink)}
  .help-item svg{flex:none;margin-top:3px}
  .help-sep{top:624px;width:1.5px;height:50px;background:var(--orange)}
  .support{left:302px;width:330px;top:708px;text-align:center;font-weight:700;font-size:15.5px;line-height:19px;color:var(--orange)}
  .contact{left:240px;width:457px;top:921px;color:var(--white);font-weight:700;text-align:center;font-style:normal}
  .contact .place{font-size:18px;line-height:26px;display:flex;justify-content:center;align-items:center;gap:9px;white-space:nowrap}
  .contact .lines{font-size:15.5px;line-height:24px;display:flex;justify-content:center;align-items:center;gap:12px;white-space:nowrap}
  .contact .lines span{display:inline-flex;align-items:center;gap:5px;white-space:nowrap}
  .contact svg{flex:none}
</style>
</head>
<body>
<main class="flyer">
  <svg class="shapes" viewBox="0 0 697 985">
    <defs>
      <linearGradient id="heroTone" x1="0" y1="0" x2="1" y2="1">
        <stop offset="0" stop-color="#8e3c18"/>
        <stop offset=".55" stop-color="#c4581f"/>
        <stop offset="1" stop-color="#ec8a3a"/>
      </linearGradient>
      <linearGradient id="pairTone" x1="0" y1="0" x2="1" y2="1">
        <stop offset="0" stop-color="#7a4a33"/>
        <stop offset="1" stop-color="#3b2418"/>
      </linearGradient>
      <linearGradient id="herdTone" x1="0" y1="0" x2="0" y2="1">
        <stop offset="0" stop-color="#8d8d7a"/>
        <stop offset="1" stop-color="#6a5a45"/>
      </linearGradient>
      <linearGradient id="chestnutTone" x1="0" y1="0" x2="1" y2="1">
        <stop offset="0" stop-color="#6f7a3d"/>
        <stop offset="1" stop-color="#a2552a"/>
      </linearGradient>
    </defs>
    <path role="img" aria-label="Photo of a herd of horses grazing in a paddock, tinted orange" d="M0 0H697V190C560 250 430 272 320 268C200 262 90 230 0 185Z" fill="url(#heroTone)"/>
    <path d="M270 272C420 282 590 250 697 190V222C590 272 430 292 270 272Z" fill="var(--orange)"/>
    <path d="M0 236C48 246 86 262 118 284L108 294C78 274 40 262 0 255Z" fill="var(--amber)"/>
    <path d="M0 275C95 300 205 340 260 520C300 650 292 820 240 985H0Z" fill="var(--orange)"/>
    <path d="M205 380C255 440 285 520 290 612L286 612C276 530 250 460 196 395Z" fill="var(--amber)"/>
    <circle cx="142" cy="359" r="110" fill="var(--orange)"/>
    <circle cx="142" cy="359" r="100" fill="var(--cream)"/>
    <path role="img" aria-label="Photo of two brown horses standing together" d="M0 800C50 770 120 775 160 785C205 795 240 830 245 880V985H0Z" fill="url(#pairTone)"/>
    <rect x="240" y="914" width="457" height="71" fill="var(--orange-light)"/>
    <g transform="rotate(-3 392 855)">
      <rect x="303" y="782" width="178" height="125" fill="var(--orange-light)"/>
      <rect role="img" aria-label="Photo of miniature ponies in a paddock" x="308" y="787" width="168" height="115" fill="url(#herdTone)"/>
    </g>
    <g transform="rotate(7 552 850)">
      <rect x="476" y="785" width="170" height="128" fill="var(--orange-light)"/>
      <rect role="img" aria-label="Photo of two chestnut horses nuzzling" x="481" y="790" width="160" height="118" fill="url(#chestnutTone)"/>
    </g>
  </svg>

  <h1 class="abs title">WILLOWMERE EQUINE<br>SANCTUARY</h1>
  <p class="abs tagline">RESCUE • REHABILITATION • SANCTUARY</p>
  <p class="abs intro">Willowmere Equine Sanctuary provides a safe and ethical refuge for horses, ponies and donkeys who have nowhere else to go. Some arrive needing rehabilitation and careful retraining, while others find permanent sanctuary here due to age, injury or behavioural needs.</p>

  <div class="abs price-badge">
    <p class="lead">SPONSORSHIP<br>STARTS FROM</p>
    <p class="amount">$15 - $25</p>
    <p class="unit">per week</p>
    <p class="amount second">$60 -$100</p>
    <p class="unit">per month.</p>
  </div>

  <p class="abs sponsor-note">One of the most meaningful ways to support our work is by sponsoring one of our residents. Each horse, pony or donkey only has one sponsor!</p>
  <h2 class="abs provide-head">Your sponsorship<br>helps provide:</h2>
  <ul class="abs provide-list">
    <li><svg width="11" height="11" viewBox="0 0 11 11"><rect x=".7" y="1.5" width="8.5" height="8.5" fill="none" stroke="#fff" stroke-width="1.2"/><path d="M2.5 5.5l2 2L10 1.5" fill="none" stroke="#fff" stroke-width="1.4"/></svg>Hay and feed</li>
    <li><svg width="11" height="11" viewBox="0 0 11 11"><rect x=".7" y="1.5" width="8.5" height="8.5" fill="none" stroke="#fff" stroke-width="1.2"/><path d="M2.5 5.5l2 2L10 1.5" fill="none" stroke="#fff" stroke-width="1.4"/></svg>Veterinary care</li>
    <li><svg width="11" height="11" viewBox="0 0 11 11"><rect x=".7" y="1.5" width="8.5" height="8.5" fill="none" stroke="#fff" stroke-width="1.2"/><path d="M2.5 5.5l2 2L10 1.5" fill="none" stroke="#fff" stroke-width="1.4"/></svg>Hoof trimming and routine<br>health care</li>
    <li><svg width="11" height="11" viewBox="0 0 11 11"><rect x=".7" y="1.5" width="8.5" height="8.5" fill="none" stroke="#fff" stroke-width="1.2"/><path d="M2.5 5.5l2 2L10 1.5" fill="none" stroke="#fff" stroke-width="1.4"/></svg>Rugs, shelter and daily care</li>
  </ul>

  <h2 class="abs mission-head">Our mission is simple:</h2>
  <p class="abs mission-body">to improve the physical and psychological wellbeing of every animal in our care.</p>
  <div class="abs divider"></div>
  <h3 class="abs focus-head">AT WILLOWMERE WE FOCUS ON:</h3>
  <ul class="abs focus-list">
    <li><svg width="9" height="9" viewBox="0 0 9 9"><circle cx="4.5" cy="4.5" r="3.8" fill="none" stroke="#333" stroke-width="1"/><path d="M2.6 4.6l1.4 1.3 3-3.2" fill="none" stroke="#333" stroke-width="1"/></svg>Rescue and rehabilitation of horses in need</li>
    <li><svg width="9" height="9" viewBox="0 0 9 9"><circle cx="4.5" cy="4.5" r="3.8" fill="none" stroke="#333" stroke-width="1"/><path d="M2.6 4.6l1.4 1.3 3-3.2" fill="none" stroke="#333" stroke-width="1"/></svg>Lifetime sanctuary for those who cannot be rehomed</li>
    <li><svg width="9" height="9" viewBox="0 0 9 9"><circle cx="4.5" cy="4.5" r="3.8" fill="none" stroke="#333" stroke-width="1"/><path d="M2.6 4.6l1.4 1.3 3-3.2" fill="none" stroke="#333" stroke-width="1"/></svg>Education and advocacy for responsible horse care</li>
    <li><svg width="9" height="9" viewBox="0 0 9 9"><circle cx="4.5" cy="4.5" r="3.8" fill="none" stroke="#333" stroke-width="1"/><path d="M2.6 4.6l1.4 1.3 3-3.2" fill="none" stroke="#333" stroke-width="1"/></svg>Equine rehabilitation services to help horses<br>recover and thrive</li>
  </ul>

  <p class="abs help-tag">HOW YOU CAN HELP</p>
  <div class="abs help-item" style="left:298px"><svg width="26" height="24" viewBox="0 0 26 24"><path d="M2 14l7 8L24 2" fill="none" stroke="var(--orange)" stroke-width="3"/></svg><span>SPONSOR A<br>HORSE</span></div>
  <div class="abs help-sep" style="left:424px"></div>
  <div class="abs help-item" style="left:432px;top:628px"><svg width="26" height="24" viewBox="0 0 26 24"><path d="M2 14l7 8L24 2" fill="none" stroke="var(--orange)" stroke-width="3"/></svg><span>MAKE A<br>DONATION</span></div>
  <div class="abs help-sep" style="left:545px"></div>
  <div class="abs help-item" style="left:552px;top:624px"><svg width="26" height="24" viewBox="0 0 26 24"><path d="M2 14l7 8L24 2" fill="none" stroke="var(--orange)" stroke-width="3"/></svg><span>SHARE OUR<br>WORK WITH<br>OTHERS</span></div>

  <p class="abs support">YOUR SUPPORT HELPS US CONTINUE TO SAY YES TO HORSES WHO NEED A SECOND CHANCE.</p>

  <address class="abs contact">
    <p class="place"><svg width="14" height="18" viewBox="0 0 14 18"><path d="M7 0a7 7 0 0 0-7 7c0 5 7 11 7 11s7-6 7-11a7 7 0 0 0-7-7z" fill="#fff"/><circle cx="7" cy="7" r="2.6" fill="var(--orange-light)"/></svg>Willowmere Park, Victoria</p>
    <p class="lines"><span><svg width="12" height="12" viewBox="0 0 12 12"><path d="M2.5 0.5l2 2.5-1.2 1.6c.8 1.7 2.2 3 3.9 3.9L8.8 7.3l2.7 2-1 2.2C5.5 11.5.5 6.5.5 1.5z" fill="#fff"/></svg>0400 519 627</span><span><svg width="13" height="10" viewBox="0 0 13 10"><rect x=".5" y=".5" width="12" height="9" fill="#fff"/><path d="M.5 .5l6 5 6-5" fill="none" stroke="var(--orange-light)" stroke-width="1.2"/></svg>clara@willowmerepark-example.org</span></p>
  </address>
</main>
</body>
</html>
```